Brightwell Wiring Needs A Logo Design

We need a logo for my new company based out of Sacramento, Ca called Brightwell Wiring. The name says it all, my electrical contracting business provides "Brightwell Craftsman Work" I'm open to any colors that pop and customers to say Wow. I would love to print my cards on metal.

Contact Information for Business Card

The card needs to have as follows
Name of company: Brightwell Wiring
My Name: Marco Delvane
Phone # 916-555-0147
CL# 4873920
Email: brightwellwiring@mailtorva.com
and a slogan that represent "BRIGHTWELL"

Requirements
Must have
• The card needs to have as follows
• Name of company: Brightwell Wiring
• My Name : Marco Delvane
• Phone # 916-555-0147
• CL# 4873920
• Email: brightwellwiring@mailtorva.com
• and a slogan that represent "BRIGHTWELL"
Nice to have
• popping colors
• electrical Arcing

```html
<!DOCTYPE html>
<html lang="en">
<head>
<meta charset="utf-8">
<title>Brightwell Wiring – Metal Business Cards</title>
<link href="https://fonts.googleapis.com/css2?family=Michroma&family=Arimo:wght@400&display=swap" rel="stylesheet">
<style>
  :root {
    --stage: #2a2a2c;
    --black-card: #1b1b1d;
    --black-card-edge: #2e2e31;
    --silver-light: #d9dadc;
    --silver-mid: #a9abae;
    --silver-dark: #7d7f83;
    --accent-red: #e3161b;
    --ink-light: #d4d4d6;
    --engrave: #5d5f63;
    --slot: #0c0c0d;
  }
  * { box-sizing: border-box; margin: 0; padding: 0; }
  html, body { width: 1200px; height: 848px; overflow: hidden; }
  body {
    background: var(--stage);
    font-family: "Arimo", Arial, sans-serif;
    position: relative;
  }
  .card {
    position: absolute;
    width: 620px;
    height: 354px;
    border-radius: 18px;
    overflow: hidden;
  }
  .card--black {
    left: 190px; top: 50px;
    background: repeating-linear-gradient(0deg, var(--black-card) 0 2px, #222225 2px 3px);
    border: 2px solid var(--black-card-edge);
  }
  .card--silver {
    left: 390px; top: 444px;
    background:
      repeating-linear-gradient(0deg, rgba(255,255,255,0.08) 0 1px, rgba(0,0,0,0.05) 1px 3px),
      linear-gradient(100deg, var(--silver-dark) 0%, var(--silver-light) 45%, var(--silver-mid) 100%);
  }
  .company {
    position: absolute; left: 48px; top: 44px;
    font-family: "Michroma", sans-serif;
    font-size: 21px; letter-spacing: 3px;
    text-transform: uppercase;
  }
  .card--black .company { color: var(--ink-light); }
  .card--silver .company { color: var(--engrave); }
  .mark-space {
    position: absolute; right: 60px; top: 40px;
    width: 120px; height: 120px;
  }
  .card--black .mark-space { background: var(--slot); }
  .card--silver .mark-space { background: #3a3b3e; }
  .person { position: absolute; left: 56px; top: 122px; }
  .person__name { font-size: 30px; line-height: 1; }
  .person__licence { font-size: 16px; margin-top: 4px; margin-left: 6px; }
  .card--black .person__name, .card--black .person__licence { color: var(--accent-red); }
  .card--silver .person__name, .card--silver .person__licence { color: var(--engrave); }
  .contact { position: absolute; left: 64px; top: 200px; font-size: 17px; }
  .contact__row { display: flex; align-items: center; gap: 10px; height: 30px; }
  .card--black .contact__row { color: var(--ink-light); }
  .card--silver .contact__row { color: var(--engrave); }
  .contact__icon { width: 20px; height: 16px; }
  .card--black .contact__icon { fill: var(--accent-red); }
  .card--silver .contact__icon { fill: var(--engrave); }
  .slots { position: absolute; left: 90px; top: 270px; width: 480px; }
  .slot {
    height: 15px; border-radius: 8px;
    background: var(--slot);
    margin-bottom: 9px;
    box-shadow: inset 0 2px 3px rgba(0,0,0,0.8);
  }
  .slot:first-child { margin-left: 0; }
</style>
</head>
<body>

  <section class="card card--black" aria-label="Business card, black finish">
    <div class="company">Brightwell Wiring</div>
    <div class="mark-space"></div>
    <div class="person">
      <div class="person__name">Marco Delvane</div>
      <div class="person__licence">CL# 4873920</div>
    </div>
    <div class="contact">
      <div class="contact__row">
        <svg class="contact__icon" viewBox="0 0 20 16" aria-hidden="true"><path d="M1 5c0-3 4-4 9-4s9 1 9 4v1h-4V4H5v2H1zM4 8l3-3h6l3 3v7H4zm6 1.5a2.5 2.5 0 1 0 0 5 2.5 2.5 0 0 0 0-5z"/></svg>
        <span>916-555-0147</span>
      </div>
      <div class="contact__row">
        <svg class="contact__icon" viewBox="0 0 20 16" aria-hidden="true"><path d="M1 2h18v12H1zm1.5 1.5L10 9l7.5-5.5z"/></svg>
        <span>brightwellwiring@mailtorva.com</span>
      </div>
    </div>
    <div class="slots">
      <div class="slot"></div><div class="slot"></div><div class="slot"></div>
    </div>
  </section>

  <section class="card card--silver" aria-label="Business card, brushed silver finish">
    <div class="company">Brightwell Wiring</div>
    <div class="mark-space"></div>
    <div class="person">
      <div class="person__name">Marco Delvane</div>
      <div class="person__licence">CL# 4873920</div>
    </div>
    <div class="contact">
      <div class="contact__row">
        <svg class="contact__icon" viewBox="0 0 20 16" aria-hidden="true"><path d="M1 5c0-3 4-4 9-4s9 1 9 4v1h-4V4H5v2H1zM4 8l3-3h6l3 3v7H4zm6 1.5a2.5 2.5 0 1 0 0 5 2.5 2.5 0 0 0 0-5z"/></svg>
        <span>916-555-0147</span>
      </div>
      <div class="contact__row">
        <svg class="contact__icon" viewBox="0 0 20 16" aria-hidden="true"><path d="M1 2h18v12H1zm1.5 1.5L10 9l7.5-5.5z"/></svg>
        <span>brightwellwiring@mailtorva.com</span>
      </div>
    </div>
    <div class="slots">
      <div class="slot"></div><div class="slot"></div><div class="slot"></div>
    </div>
  </section>

</body>
</html>
```